Supplement label for Brain health

I need a design for a supplement this supplement is a brain boost supplement.

The Name is Cortiva Plus.

I have attached other labels I like. This is for 50 plus demographic so the lettering needs to be easy to read and stand out. I have attached a dummy label template that once the winner is choosen then they will get the real supplement facts etc.

Clean desgin easy to read.

This file must be finished in AI format.

Target Market(s)

50 plus 70 percent female 30 percent male

Industry/Entity Type

Supplement

Font styles to use
Other font styles liked:
• Myrid pro maybe

Requirements
Must have
• easy to read text so no colors that hide text or hard to read.

```html
<!DOCTYPE html>
<html lang="en">
<head>
<meta charset="utf-8">
<title>Cortiva Plus – Supplement Label</title>
<link rel="stylesheet" href="https://fonts.googleapis.com/css2?family=Arimo:ital,wght@0,400;0,700;1,400&family=Roboto+Condensed:ital,wght@0,300;0,400;0,700;1,400&display=swap">
<style>
  :root{
    --ink:#050608;
    --blue:#1ba3e0;
    --blue-deep:#0d5f9e;
    --white:#ffffff;
    --page:#f2f3f5;
    --cond:"Roboto Condensed", "Arial Narrow", sans-serif;
    --body:"Arimo", Arial, sans-serif;
  }
  *{box-sizing:border-box;margin:0;padding:0}
  html,body{width:960px;height:1200px;overflow:hidden;background:var(--page)}
  .canvas{position:relative;width:960px;height:1200px}
  .label{position:absolute;left:19px;top:369px;width:922px;height:462px;background:var(--ink);overflow:hidden;color:var(--white)}

  /* left info panel */
  .directions{position:absolute;left:18px;top:40px;width:262px;font-family:var(--body);font-size:9.3px;line-height:1.22;text-align:justify}
  .directions p{margin-bottom:10px}
  .directions b{font-weight:700}
  .disclaimer{position:absolute;left:21px;top:290px;width:216px;background:var(--white);color:var(--ink);font-family:var(--body);font-weight:700;font-size:6.6px;line-height:1.25;padding:2px 3px}
  .distributor{position:absolute;left:21px;top:340px;font-family:var(--cond);font-weight:700;font-size:12px;line-height:1.35}

  /* front panel */
  .natural-tab{position:absolute;left:310px;top:0;width:39px;height:149px;background:var(--blue);display:flex;align-items:center;justify-content:center}
  .natural-tab span{transform:rotate(-90deg);white-space:nowrap;font-family:var(--cond);font-size:29px;color:var(--white)}
  .brand{position:absolute;display:flex;align-items:center;gap:6px;font-family:var(--cond);font-weight:400;color:var(--white)}
  .brand-front{left:366px;top:36px}
  .brand-dot{width:22px;height:22px;border-radius:50%;background:var(--white)}
  .brand-name{line-height:1}
  .brand-front .brand-name .line1{font-size:25px;letter-spacing:.5px;display:block}
  .brand-front .brand-name .line2{font-size:12px;letter-spacing:7px;display:block;margin-top:1px}
  .product-name{position:absolute;left:354px;top:158px;font-family:var(--cond);font-weight:700;line-height:1.05;font-size:46px}
  .product-name .top{color:var(--white);display:block}
  .product-name .bottom{color:var(--blue);display:block}
  .benefits{position:absolute;left:356px;top:277px;width:158px;border-top:1px dotted var(--blue);border-bottom:1px dotted var(--blue);padding:5px 0 4px;font-family:var(--cond);font-style:italic;font-size:11.3px;line-height:1.38;list-style:none;letter-spacing:.2px}
  .seal{position:absolute;width:38px;height:38px;border-radius:50%;border:2px solid var(--blue);background:var(--blue-deep)}
  .count{position:absolute;left:360px;top:405px;font-family:var(--cond);font-size:19px;line-height:1.3}
  .brain-art{position:absolute;left:535px;top:80px;width:150px;height:262px;border-radius:45% 40% 30% 40%;background:radial-gradient(ellipse at 45% 35%, #5fb8f0 0%, #1f6fc0 45%, #0a2f66 75%, rgba(5,6,8,0) 100%)}
  .focus-list{position:absolute;left:516px;top:360px;list-style:none;font-family:var(--cond);font-weight:300;font-size:18.5px;color:var(--blue);line-height:1.22}
  .focus-list li{display:flex;align-items:center;gap:6px}
  .focus-list svg{width:10px;height:10px}

  /* facts panel */
  .facts-panel{position:absolute;left:702px;top:0;width:220px;height:462px;background:var(--blue);color:var(--ink)}
  .brand-back{left:46px;top:30px;color:var(--ink)}
  .brand-back .brand-dot{width:16px;height:16px;background:var(--ink)}
  .brand-back .line1{font-size:18px;display:block}
  .brand-back .line2{font-size:8.5px;letter-spacing:5px;display:block}
  .facts{position:absolute;left:15px;top:67px;width:191px;background:var(--white);border:1px solid var(--ink);padding:2px 4px;font-family:var(--body);font-size:7.4px;line-height:1.15}
  .facts h2{font-family:var(--body);font-weight:700;font-size:17px;line-height:1;border-bottom:1px solid var(--ink);padding-bottom:1px}
  .facts .serving{padding:1px 0 2px 2px;border-bottom:4px solid var(--ink)}
  .facts .head{font-size:5.8px;border-bottom:1px solid var(--ink);padding:1px 0 1px 2px}
  .facts table{width:100%;border-collapse:collapse}
  .facts td{vertical-align:top;padding:0 0 0 2px;border-bottom:1px solid var(--ink)}
  .facts td.amt{text-align:right;white-space:nowrap;width:40px;padding-right:4px}
  .facts tr:last-child td{border-bottom:3px solid var(--ink)}
  .facts .note{padding:1px 2px}
  .other{position:absolute;left:16px;top:252px;width:194px;font-family:var(--body);font-size:7.4px;line-height:1.15}
  .other b{font-weight:700}
  .warning{position:absolute;left:16px;top:295px;width:194px;font-family:var(--body);font-weight:700;font-size:7.4px;line-height:1.15}
  .facts-panel .seal{border-color:var(--white);background:var(--white);opacity:.9}
</style>
</head>
<body>
<div class="canvas">
  <section class="label">

    <div class="directions">
      <p><b>SUGGESTED USE:</b> 1 capsule taken 1 to 2 times daily preferably with meals or as directed by a healthcare professional.</p>
      <p><b>CAUTION:</b> Do not exceed recommended dose. St. John's Wort may contribute to photosensitivity resulting in skin irritation and redness in persons exposed to strong sunlight or tanning booths. Avoid use in patients at risk of bleeding, taking anticoagulants, or with clotting disorders, based on case reports of bleeding. Discontinue use 2-3 weeks prior to some surgical and dental procedures due to increased risk of bleeding. Avoid use in couples who are trying to conceive, based on theoretical reduction of fertility. Pregnant or nursing mothers, children under 18, individuals with history of seizure, taking MAO inhibiting drugs, or with a known medical condition should consult a physician before using this or any dietary supplement. This product is manufactured and packaged in a facility which may also process milk, soy, wheat, egg, peanuts, tree nuts, fish and crustacean shellfish.</p>
    </div>
    <p class="disclaimer">†These statements have not been evaluated by the Food &amp; Drug Administration. This product is not intended to diagnose, treat, cure or prevent any disease.</p>
    <p class="distributor">Distributed by:<br>Company Name<br>Full Address and Phone</p>

    <div class="natural-tab"><span>All Natural</span></div>
    <div class="brand brand-front">
      <span class="brand-dot"></span>
      <span class="brand-name"><span class="line1">HALVANE</span><span class="line2">NUTRITION</span></span>
    </div>
    <div class="brain-art" role="img" aria-label="Blue illustration of a human head in profile with gears inside"></div>
    <h1 class="product-name"><span class="top">CORTIVA</span><span class="bottom">PLUS</span></h1>
    <ul class="benefits">
      <li>ASSIST MENTAL CLARITY</li>
      <li>FEEL FOCUSED AND ALERT</li>
      <li>HELP &amp; SUPPORT YOUR BRAIN</li>
      <li>BOOST YOUR PRODUCTIVITY</li>
    </ul>
    <span class="seal" style="left:357px;top:357px"></span>
    <span class="seal" style="left:400px;top:357px"></span>
    <span class="seal" style="left:443px;top:357px"></span>
    <p class="count">30 capsules<br>Dietary Supplement</p>
    <ul class="focus-list">
      <li><svg viewBox="0 0 10 10"><path d="M1 1 L8 4.5 L1 8 M1 4 L8 7.5" fill="none" stroke="#ffffff" stroke-width="1.4"/></svg>MEMORY</li>
      <li><svg viewBox="0 0 10 10"><path d="M1 1 L8 4.5 L1 8 M1 4 L8 7.5" fill="none" stroke="#ffffff" stroke-width="1.4"/></svg>FOCUS</li>
      <li><svg viewBox="0 0 10 10"><path d="M1 1 L8 4.5 L1 8 M1 4 L8 7.5" fill="none" stroke="#ffffff" stroke-width="1.4"/></svg>CLARITY</li>
    </ul>

    <aside class="facts-panel">
      <div class="brand brand-back">
        <span class="brand-dot"></span>
        <span class="brand-name"><span class="line1">HALVANE</span><span class="line2">NUTRITION</span></span>
      </div>
      <div class="facts">
        <h2>Supplement Facts</h2>
        <p class="serving">Serving Size 1 Capsule<br>Servings Per Container: 30</p>
        <p class="head">Amt Per Serv. &nbsp;%DV/RDI</p>
        <table>
          <tr><td><i>Ginkgo biloba</i> Leaf (24% extract)</td><td class="amt">50mg *</td></tr>
          <tr><td>Phosphatidylserine 4% Complex (consisting of Lecithin and Phosphatidylserine)</td><td class="amt">125mg *</td></tr>
          <tr><td>N-Acetyl L-Carnitine HCl</td><td class="amt">50mg *</td></tr>
          <tr><td>St. John's Wort (0.3% extract) (flower heads)</td><td class="amt">250mg *</td></tr>
          <tr><td>L-Glutamine</td><td class="amt">150mg *</td></tr>
          <tr><td><i>Bacopa monnieri</i> Leaf Extract (20% bacosides)</td><td class="amt">120mg *</td></tr>
          <tr><td>Vinpocetine (seeds)</td><td class="amt">2mg *</td></tr>
          <tr><td>Huperzine-A (aerial plant)</td><td class="amt">10mcg *</td></tr>
        </table>
        <p class="note">*Daily Value not established.</p>
      </div>
      <p class="other"><b>Other ingredients:</b> Gelatin (bovine), microcrystalline cellulose, vegetable magnesium stearate, and silicon dioxide.<br><b>ALLERGEN WARNING: CONTAINS SOY (LECITHIN).</b></p>
      <p class="warning">KEEP OUT OF THE REACH OF CHILDREN.<br>DO NOT USE IF SAFETY SEAL IS DAMAGED OR MISSING. STORE IN A COOL, DRY PLACE.</p>
      <span class="seal" style="left:40px;top:335px"></span>
      <span class="seal" style="left:91px;top:335px"></span>
      <span class="seal" style="left:141px;top:335px"></span>
    </aside>

  </section>
</div>
</body>
</html>
```